Postcard Design

We are an upscale, full service real estate boutique based in Mt. Pleasant, SC. We will be having a Grand Opening of our beautiful, new office complete with high end custom home architecture and design. I will attach photos for your review. I would like to come up with a medium postcard to be mailed to clientele of Mt. Pleasant. Home prices between $300,000 - $2.2 million. The customers can call our office for the Grand Opening Listing Promotion or stop by our grand opening. We will have drawings for door prizes that include services at Brindlecove Day Spa, Copper Kettle Pies gift certificates, and they can register to win a cruise with a listing presentation. Our Grand Opening will be a couple of different dates, April 7, 2016 and April 21, 2016. I will want an order that lists the 7th and another order that will list the 21. The look should have a very "relaxing, beach" feel, but not Myrtle Beach...should reflect colors of the ocean, like you are on vacation. I will include logos and pics for your review. Thank you!

```html
<!DOCTYPE html>
<html lang="en">
<head>
<meta charset="utf-8">
<title>Grand Opening Postcard</title>
<link href="https://fonts.googleapis.com/css2?family=Open+Sans:wght@400;600;700;800&display=swap" rel="stylesheet">
<style>
:root{
  --navy:#0f4a93;
  --deep:#0b3f86;
  --sky:#14a9d9;
  --aqua:#00a9d8;
  --orange:#ea4a28;
  --ink:#1a4c8f;
  --paper:#ffffff;
  --cream:#fbfaf7;
  --stage:#2b2b2b;
  --rule:#c9c9c9;
}
*{margin:0;padding:0;box-sizing:border-box}
html,body{width:960px;height:1200px;overflow:hidden;background:var(--stage)}
body{font-family:"Open Sans",Arial,sans-serif;position:relative}
.card{position:absolute;left:120px;width:720px;background:var(--paper);overflow:hidden}
.front{top:30px;height:558px;background:var(--cream)}
.back{top:608px;height:560px}
.layer{position:absolute;left:0;top:0}
.abs{position:absolute}
.headline{font-weight:800;font-size:27px;color:#fff;letter-spacing:.2px;line-height:1}
.dates{font-weight:700;font-size:19px;color:#fff;line-height:1}
.brand{display:flex;flex-direction:column;align-items:center;justify-content:center;border-radius:50%;background:#fff;text-align:center;color:var(--sky);font-weight:700}
.brand .dot{width:34px;height:34px;border-radius:50%;background:var(--sky);margin-bottom:8px}
.brand .name{font-size:22px;letter-spacing:1.5px;line-height:1.1}
.brand .sub{font-size:10px;letter-spacing:3px;line-height:1.4}
.photo-circle{border-radius:50%;border:3px solid #fff;overflow:hidden}
.price-pill{background:#2f5bb0;color:#fff;font-size:19px;line-height:26px;text-align:center;border-radius:0 18px 18px 0;padding:4px 10px 4px 18px}
.call{color:var(--ink);font-size:20px;font-weight:600;text-align:center;line-height:26px}
.phone-front{color:var(--orange);font-weight:800;font-size:32px;text-align:center;letter-spacing:.5px}
.url-pill{background:var(--deep);color:#fff;font-weight:600;font-size:17px;text-align:center;border-radius:16px;line-height:31px}
.register{color:var(--ink);font-size:18px;line-height:26px}
.register b{font-weight:800}
.back-panel{position:absolute;left:0;top:0;width:349px;height:560px;background:var(--aqua)}
.back-call{color:var(--deep);font-size:17px;font-weight:600;text-align:center;line-height:22px}
.contact-band{position:absolute;left:0;top:424px;width:349px;height:90px;background:var(--deep);color:#fff;text-align:center}
.contact-band .phone{font-weight:800;font-size:33px;padding-top:14px;line-height:1.1}
.contact-band .url{font-weight:600;font-size:18px;line-height:1.4}
.stamp{position:absolute;left:624px;top:26px;width:70px;height:74px;border:1.5px solid var(--rule)}
.address-line{position:absolute;left:418px;width:248px;height:2px;background:var(--rule)}
</style>
</head>
<body>

<section class="card front" aria-label="Postcard front">
  <div class="layer" role="img" aria-label="Photo of a couple relaxing in beach chairs on white sand facing a turquoise sea with overwater huts"
       style="width:720px;height:430px;background:linear-gradient(180deg,#cfe3f2 0%,#eaf3f8 30%,#7fd3e3 42%,#bfeaee 56%,#efece4 72%,#e9e2d3 100%)"></div>
  <svg class="layer" width="720" height="558" viewBox="0 0 720 558" aria-hidden="true">
    <path d="M0 0H720V150C690 110 660 60 560 40C470 25 400 80 330 105C240 135 120 120 0 88Z" fill="#0f4a93"/>
    <path d="M0 88C120 120 240 135 330 105C400 80 470 25 560 40C610 48 650 62 690 45C600 70 520 50 460 75C380 110 300 150 200 140C120 132 60 118 0 100Z" fill="#14a9d9"/>
    <path d="M690 45C700 80 712 110 720 150V210C710 180 700 160 690 150Z" fill="#14a9d9"/>
    <path d="M0 470C140 450 300 420 420 398C520 380 620 370 720 372V558H0Z" fill="#fbfaf7"/>
  </svg>
  <div class="abs headline" style="left:30px;top:30px">GRAND OPENING ON</div>
  <div class="abs dates" style="left:34px;top:61px">April 7, 2016 &amp; April 21, 2016</div>
  <div class="abs brand" style="left:512px;top:18px;width:188px;height:188px">
    <span class="dot"></span>
    <span class="name">SALTMARSH</span>
    <span class="sub">REAL ESTATE</span>
  </div>
  <div class="abs price-pill" style="left:160px;top:382px;width:252px">Home prices between<br>$300,000 - $2.2 million.</div>
  <div class="abs photo-circle" role="img" aria-label="Photo of a pale blue two-storey coastal home among trees"
       style="left:18px;top:328px;width:148px;height:148px;background:linear-gradient(180deg,#9fc6e6 0%,#b8cbe0 40%,#8aa6c2 70%,#6f8c4f 100%)"></div>
  <div class="abs call" style="left:420px;top:397px;width:248px">Call us for Grand<br>Opening Promotion</div>
  <div class="abs phone-front" style="left:420px;top:452px;width:248px">843-555-0172</div>
  <div class="abs url-pill" style="left:408px;top:501px;width:272px">www.saltmarshrealestate.com</div>
  <div class="abs register" style="left:22px;top:480px">You can register to win<br><b>a cruise with a listing presentation</b></div>
</section>

<section class="card back" aria-label="Postcard back">
  <div class="back-panel"></div>
  <div class="layer" role="img" aria-label="Photo of a pale blue two-storey coastal home with shutters, surrounded by trees"
       style="width:349px;height:240px;background:linear-gradient(180deg,#8fc0ea 0%,#a9c7e2 35%,#93acc6 60%,#6f8a4c 100%)"></div>
  <svg class="layer" width="349" height="300" viewBox="0 0 349 300" aria-hidden="true">
    <path d="M0 170C60 160 140 190 180 230C220 262 290 250 349 190V300H0Z" fill="#0f4a93"/>
    <path d="M0 182C60 175 140 205 180 240C220 270 290 262 349 210V300H0Z" fill="#00a9d8"/>
  </svg>
  <div class="abs brand" style="left:20px;top:148px;width:144px;height:144px">
    <span class="dot" style="width:26px;height:26px;margin-bottom:6px"></span>
    <span class="name" style="font-size:17px">SALTMARSH</span>
    <span class="sub" style="font-size:8px">REAL ESTATE</span>
  </div>
  <div class="abs headline" style="left:0;width:349px;text-align:center;top:304px">GRAND OPENING ON</div>
  <div class="abs dates" style="left:0;width:349px;text-align:center;top:339px">April 7, 2016 &amp; April 21, 2016</div>
  <div class="abs back-call" style="left:0;width:349px;top:370px">Call us for Grand Opening<br>Promotion &amp; Registration</div>
  <div class="contact-band">
    <div class="phone">843-555-0172</div>
    <div class="url">www.saltmarshrealestate.com</div>
  </div>
  <div class="stamp"></div>
  <div class="address-line" style="top:308px"></div>
  <div class="address-line" style="top:349px"></div>
  <div class="address-line" style="top:391px"></div>
  <div class="address-line" style="top:432px"></div>
</section>

</body>
</html>
```